I need an Office Furniture selling website

My office furniture store is driven by creativity and innovation. With this i am searching for an industry standard website for my office furniture and items selling website. I sell a wide range of office furniture items such as chairs, tables, burglary, cotton, wardrobe, etc. There will be a category for each of the items i sell. My business is based in the United States and services only US based residents. I don't accept online payments and customers are to pay on delivery of items. The website is to have images of the items i sell. I would like brown, black and golden colors because those are the colors furniture mostly make use of. Designs submitted should be unique.

Industry/Entity Type

Furniture Store

Coding

Coded - Design and coding required

```html
<!DOCTYPE html>
<html lang="en">
<head>
<meta charset="utf-8">
<title>Harwell Office Furniture</title>
<link rel="stylesheet" href="https://fonts.googleapis.com/css2?family=Lora:wght@400;700&family=Open+Sans:wght@400;600;700&family=Raleway:wght@400;500;700;800&display=swap">
<style>
:root{
  --brown:#7a3510;
  --brown-dark:#5a2208;
  --brown-deep:#461905;
  --gold:#e8bf2e;
  --gold-soft:#efcd4f;
  --black:#000;
  --ink:#222;
  --grey:#888;
  --line:#dcdcdc;
  --white:#fff;
}
*{margin:0;padding:0;box-sizing:border-box}
html,body{width:1200px;height:2903px;overflow:hidden;background:var(--white)}
body{font-family:"Open Sans",Arial,sans-serif;color:var(--ink);position:relative}
.abs{position:absolute}
a{color:inherit;text-decoration:none}

/* header */
.site-header{position:absolute;left:0;top:0;width:1200px;height:120px}
.brand{left:100px;top:36px;font-family:"Lora",Georgia,serif;font-size:46px;color:var(--brown);line-height:1}
.account-links{right:100px;top:16px;font-size:11px;color:var(--gold);letter-spacing:.5px}
.account-links span{margin:0 6px}
.search{left:414px;top:60px;width:336px;height:34px;display:flex}
.search-field{flex:1;border:1px solid #ccc;border-right:none;font-size:11px;color:#aaa;padding:9px 10px}
.search-btn{width:40px;background:var(--brown);display:flex;align-items:center;justify-content:center}
.phone{left:945px;top:64px;font-size:18px;color:var(--ink);display:flex;align-items:center;gap:8px}

/* nav */
.main-nav{position:absolute;left:0;top:120px;width:1200px;height:50px;background:var(--black)}
.main-nav a{position:absolute;top:0;height:50px;line-height:50px;text-align:center;color:var(--white);font-size:14px;font-weight:600;border-right:1px solid #333}
.main-nav a.active{background:var(--gold);border-right:none}

/* hero */
.hero{position:absolute;left:0;top:170px;width:1200px;height:450px;background:linear-gradient(120deg,#5b5149 0%,#8b7f73 35%,#b8ab9a 60%,#6f5c47 100%)}
.hero-card{left:722px;top:66px;width:333px;height:290px;background:rgba(232,191,46,.93);outline:6px solid rgba(240,210,110,.55);text-align:center;color:var(--white);font-family:"Raleway",sans-serif;padding-top:44px}
.hero-card .kicker{font-size:22px;font-weight:500;line-height:29px}
.hero-card h1{font-size:27px;font-weight:800;line-height:31px;margin-top:14px}
.btn-brown{display:inline-block;background:var(--brown);color:var(--white);font-family:"Open Sans",sans-serif;font-size:14px;font-weight:600;padding:11px 34px;margin-top:24px}
.slide-arrow{top:190px}

/* categories */
.category-strip{position:absolute;left:0;top:620px;width:1200px;height:115px;background:linear-gradient(#fafafa,#e8e8e8);border-top:1px solid #ddd;border-bottom:1px solid #ddd}
.category-title{left:133px;top:32px;font-family:"Raleway",sans-serif;color:var(--brown);font-size:20px;font-weight:500}
.category-title small{display:block;font-family:"Open Sans",sans-serif;font-size:11px;color:#666;margin-top:4px;padding-left:12px}
.category-cell{top:0;height:115px;display:flex;align-items:center;justify-content:center;border-left:1px solid #d6d6d6}

/* tiles */
.tile{top:768px;width:306px;height:236px}
.tile-label{position:absolute;left:0;bottom:0;width:100%;height:48px;line-height:48px;text-align:center;font-size:20px}
.promo{top:1030px;height:282px;text-align:center;color:var(--white);padding-top:82px}
.promo h2{font-family:"Raleway",sans-serif;font-weight:800;font-size:31px;line-height:34px}
.promo p{font-family:"Lora",serif;font-size:21px;margin-top:2px}
.btn-outline{display:inline-block;border:2px solid var(--white);font-size:13px;font-weight:600;padding:8px 26px;margin-top:18px}

/* arrivals */
.section-title{left:0;width:1200px;text-align:center;font-family:"Lora",serif;font-size:28px}
.product{top:1409px;width:241px;height:333px;border:1px solid var(--line);text-align:center}
.product-shot{margin:22px auto 0;width:190px;height:190px}
.product h3{font-size:16px;font-weight:600;margin-top:30px}
.product p{font-size:11px;color:var(--grey);margin-top:2px}
.product .price{font-size:23px;font-weight:600;margin-top:10px;color:#222}

.bestsell{left:106px;top:1806px;width:987px;height:346px;border:1px solid #ccc;background:linear-gradient(180deg,#f3f3f1,#e9e7e2 60%,#f1f0ee);text-align:center;padding-top:102px}
.bestsell h4{font-family:"Lora",serif;font-weight:400;font-size:30px;color:#555}
.bestsell h2{font-family:"Raleway",sans-serif;font-weight:500;font-size:31px;color:#333;margin-top:2px}
.btn-black{display:inline-block;background:var(--black);color:var(--white);font-size:14px;font-weight:600;padding:11px 29px;margin-top:24px}

/* reviews */
.reviews{position:absolute;left:0;top:2203px;width:1200px;height:348px;background:var(--gold-soft)}
.reviews h2{position:absolute;top:26px;width:100%;text-align:center;font-family:"Lora",serif;font-weight:400;font-size:26px;color:var(--white)}
.avatar{border-radius:50%;border:4px solid var(--white);background:linear-gradient(#bdb6ad,#807a72)}
.quote{left:180px;top:202px;width:840px;text-align:center;font-family:"Raleway",sans-serif;font-size:17px;line-height:25px;color:#6a5325}
.qmark{font-family:"Lora",serif;font-size:40px;color:#5a4520;line-height:0;position:relative}
.qmark.open{top:6px;margin-right:4px}
.qmark.close{top:16px;margin-left:4px}
.author{top:266px;width:100%;text-align:center;font-style:italic;font-size:19px;line-height:26px;color:#5a4520}
.stars{top:300px;width:100%;text-align:center}

/* footer */
.site-footer{position:absolute;left:0;top:2551px;width:1200px;height:284px;background:var(--brown-dark);color:var(--white)}
.footer-col{top:64px}
.footer-col h5{font-family:"Lora",serif;font-weight:400;font-size:17px;margin-bottom:8px}
.footer-col li{list-style:none;font-size:12.5px;line-height:27px}
.email-field{left:865px;top:92px;width:234px;height:30px;background:var(--white);color:#999;font-size:11px;padding:7px 10px 0 32px}
.subscribe{left:865px;top:134px;width:116px;height:30px;background:var(--gold);font-size:12px;font-weight:600;text-align:center;line-height:30px}
.social{top:180px;width:34px;height:34px;border:2px solid var(--white);border-radius:50%}
.paycard{top:208px;width:40px;height:26px;border-radius:3px}
.copyright{position:absolute;left:0;top:2835px;width:1200px;height:68px;background:var(--brown-deep);color:#c9a993;text-align:center;font-size:12px;line-height:68px}
</style>
</head>
<body>

<header class="site-header">
  <div class="abs brand">Harwell</div>
  <div class="abs account-links">MY ACCOUNT<span>|</span>LOGIN<span>|</span>REGISTER</div>
  <div class="abs search">
    <div class="search-field">Search here</div>
    <div class="search-btn"><svg width="18" height="18" viewBox="0 0 18 18"><circle cx="7.5" cy="7.5" r="5.5" fill="none" stroke="#fff" stroke-width="2"/><line x1="11.5" y1="11.5" x2="16" y2="16" stroke="#fff" stroke-width="2.4"/></svg></div>
  </div>
  <div class="abs phone"><svg width="18" height="18" viewBox="0 0 24 24"><path fill="#e8bf2e" d="M6.6 10.8a15 15 0 0 0 6.6 6.6l2.2-2.2c.3-.3.7-.4 1-.2 1.1.4 2.3.6 3.6.6.6 0 1 .4 1 1V20c0 .6-.4 1-1 1A17 17 0 0 1 3 4c0-.6.4-1 1-1h3.5c.6 0 1 .4 1 1 0 1.3.2 2.5.6 3.6.1.3 0 .7-.2 1z"/></svg>(555) 014 2290</div>
</header>

<nav class="main-nav">
  <a class="active" style="left:104px;width:96px">HOME</a>
  <a style="left:200px;width:142px">ABOUT US</a>
  <a style="left:342px;width:173px">NEW PRODUTS</a>
  <a style="left:515px;width:175px">ALL CATEGORY</a>
  <a style="left:690px;width:163px">BEST SELLING</a>
  <a style="left:853px;width:134px">SHOP NOW</a>
  <a style="left:987px;width:139px;border-right:none">CONTACT</a>
</nav>

<section class="hero" role="img" aria-label="Open-plan office with rows of dark desks and black swivel chairs">
  <svg class="abs slide-arrow" style="left:106px" width="22" height="40" viewBox="0 0 22 40"><polyline points="18,4 4,20 18,36" fill="none" stroke="#fff" stroke-width="4"/></svg>
  <svg class="abs slide-arrow" style="left:1080px" width="22" height="40" viewBox="0 0 22 40"><polyline points="4,4 18,20 4,36" fill="none" stroke="#fff" stroke-width="4"/></svg>
  <div class="abs hero-card">
    <div class="kicker">HARWELL OFFICE<br>FURNITURE</div>
    <h1>THAT'S NEW<br>FOUND ANY WHERE</h1>
    <a class="btn-brown">SHOP NOW</a>
  </div>
</section>

<section class="category-strip">
  <div class="abs category-title">OUR CATEGORY<small>CHOOSE YOUR ONE</small></div>
  <div class="abs category-cell" style="left:300px;width:135px;border-left:none">
    <svg width="60" height="54" viewBox="0 0 60 54" fill="#7a3510"><rect x="2" y="2" width="30" height="50"/><rect x="6" y="8" width="22" height="12" fill="#f0f0f0"/><rect x="6" y="26" width="22" height="10" fill="#f0f0f0"/><rect x="32" y="30" width="26" height="22"/><rect x="36" y="16" width="6" height="14"/><rect x="46" y="10" width="8" height="20"/></svg>
  </div>
  <div class="abs category-cell" style="left:435px;width:136px">
    <svg width="70" height="44" viewBox="0 0 70 44" fill="#7a3510"><polygon points="2,14 40,4 68,12 30,22"/><polygon points="4,16 10,16 10,40 4,40"/><polygon points="42,20 66,14 66,36 42,42"/></svg>
  </div>
  <div class="abs category-cell" style="left:571px;width:137px">
    <svg width="46" height="52" viewBox="0 0 46 52" fill="none" stroke="#7a3510" stroke-width="4"><rect x="3" y="3" width="40" height="42"/><line x1="23" y1="3" x2="23" y2="45"/><line x1="6" y1="50" x2="6" y2="45"/><line x1="40" y1="50" x2="40" y2="45"/><line x1="18" y1="20" x2="18" y2="28"/><line x1="28" y1="20" x2="28" y2="28"/></svg>
  </div>
  <div class="abs category-cell" style="left:708px;width:128px">
    <svg width="46" height="58" viewBox="0 0 46 58" fill="#7a3510"><rect x="13" y="2" width="20" height="22" rx="4"/><rect x="8" y="28" width="30" height="6"/><rect x="2" y="20" width="5" height="12"/><rect x="39" y="20" width="5" height="12"/><rect x="21" y="34" width="4" height="12"/><rect x="6" y="46" width="34" height="4"/><circle cx="7" cy="53" r="3"/><circle cx="39" cy="53" r="3"/><circle cx="23" cy="53" r="3"/></svg>
  </div>
  <div class="abs category-cell" style="left:836px;width:130px">
    <svg width="64" height="52" viewBox="0 0 64 52" fill="none" stroke="#7a3510" stroke-width="4"><line x1="4" y1="2" x2="4" y2="50"/><line x1="60" y1="2" x2="60" y2="50"/><line x1="4" y1="10" x2="60" y2="10"/><line x1="4" y1="40" x2="60" y2="40"/><line x1="15" y1="10" x2="15" y2="40"/><line x1="26" y1="10" x2="26" y2="40"/><line x1="38" y1="10" x2="38" y2="40"/><line x1="49" y1="10" x2="49" y2="40"/></svg>
  </div>
  <div class="abs category-cell" style="left:966px;width:110px">
    <svg width="54" height="50" viewBox="0 0 54 50" fill="#7a3510"><rect x="10" y="2" width="34" height="26" rx="6"/><rect x="2" y="16" width="12" height="28" rx="4"/><rect x="40" y="16" width="12" height="28" rx="4"/><rect x="12" y="30" width="30" height="14"/><rect x="6" y="44" width="4" height="5"/><rect x="44" y="44" width="4" height="5"/></svg>
  </div>
</section>

<section class="tiles">
  <div class="abs tile" style="left:126px;background:linear-gradient(#cfcfcd,#e2e2e0)" role="img" aria-label="Red lounge chair against a concrete wall">
    <div class="tile-label" style="background:rgba(255,255,255,.85);color:#333">Best Sellings</div>
  </div>
  <div class="abs tile" style="left:451px;background:linear-gradient(#dcdad6,#b49067)" role="img" aria-label="Wooden office desk with a beige leather chair">
    <div class="tile-label" style="background:rgba(232,191,46,.9);color:#fff">New Special Deals</div>
  </div>
  <div class="abs tile" style="left:776px;background:linear-gradient(#e6e4e0,#a4683a)" role="img" aria-label="Wooden office tables with black chairs">
    <div class="tile-label" style="background:rgba(30,30,30,.85);color:#fff">Shop Tables</div>
  </div>

  <div class="abs promo" style="left:126px;width:470px;background:linear-gradient(135deg,#6d5a48,#9b8469 55%,#5a4a3c)" role="img" aria-label="Office corner with red chairs, a table and wooden shelving">
    <h2>NEW EXCLUSIVE SET OF</h2><p>CHAIR &amp; TABLE</p><a class="btn-outline">CLICK HERE</a>
  </div>
  <div class="abs promo" style="left:610px;width:472px;background:linear-gradient(135deg,#5c5855,#8d8680 50%,#3f3b39)" role="img" aria-label="Executive leather chair at a dark desk with a laptop">
    <h2>PROIN NULLA NONUMMY</h2><p>DICTUM EGET FERMENTU</p><a class="btn-outline">CLICK HERE</a>
  </div>
</section>

<h2 class="abs section-title" style="top:1346px">NEW ARRIVALS</h2>

<section class="arrivals">
  <div class="abs product" style="left:103px"><div class="product-shot" role="img" aria-label="Round meeting table with six chairs" style="background:radial-gradient(circle,#9a8d84 0%,#e8e4e0 55%,#fff 75%)"></div><h3>Product Name</h3><p>Praesent elementum elit tellus nec</p><div class="price">$25.99</div></div>
  <div class="abs product" style="left:354px"><div class="product-shot" role="img" aria-label="Black leather executive chair" style="background:radial-gradient(circle,#3a3634 0%,#c9c5c2 55%,#fff 75%)"></div><h3>Product Name</h3><p>Praesent elementum elit tellus nec</p><div class="price">$39.99</div></div>
  <div class="abs product" style="left:604px"><div class="product-shot" role="img" aria-label="Light wood desk with a black task chair" style="background:radial-gradient(circle,#b48f62 0%,#e4ddd4 55%,#fff 75%)"></div><h3>Product Name</h3><p>Praesent elementum elit tellus nec</p><div class="price">$35.99</div></div>
  <div class="abs product" style="left:852px"><div class="product-shot" role="img" aria-label="White office chair on a black base" style="background:radial-gradient(circle,#bdb8b2 0%,#ebe9e6 55%,#fff 75%)"></div><h3>Product Name</h3><p>Praesent elementum elit tellus nec</p><div class="price">$45.99</div></div>
</section>

<section class="abs bestsell" role="img" aria-label="Faded bright office room with desks and chairs">
  <h4>OU R BEST SELLINGS</h4>
  <h2>PROIN NULLA ARCU NONUMMY LUCTUS</h2>
  <a class="btn-black">VIEW MORE</a>
</section>

<section class="reviews">
  <h2>CUSTOMER REVIEWS</h2>
  <svg class="abs" style="left:122px;top:122px" width="18" height="34" viewBox="0 0 18 34"><polyline points="15,3 3,17 15,31" fill="none" stroke="#fff" stroke-width="3"/></svg>
  <svg class="abs" style="left:1058px;top:122px" width="18" height="34" viewBox="0 0 18 34"><polyline points="3,3 15,17 3,31" fill="none" stroke="#fff" stroke-width="3"/></svg>
  <div class="abs avatar" style="left:413px;top:96px;width:76px;height:76px" role="img" aria-label="Customer portrait"></div>
  <div class="abs avatar" style="left:471px;top:92px;width:86px;height:86px" role="img" aria-label="Customer portrait"></div>
  <div class="abs avatar" style="left:647px;top:92px;width:86px;height:86px" role="img" aria-label="Customer portrait"></div>
  <div class="abs avatar" style="left:717px;top:96px;width:76px;height:76px" role="img" aria-label="Customer portrait"></div>
  <div class="abs avatar" style="left:540px;top:72px;width:120px;height:120px;background:linear-gradient(#d8cbb9,#a6978a)" role="img" aria-label="Portrait of the featured reviewer"></div>
  <div class="abs quote"><span class="qmark open">&ldquo;</span>Vivamus porttitor purus nisi eleifend libero a tempus libero lectus feugiat felis Morbi diam mauris viverra in gravida eu mattis in ante Morbi eget arcu Morbi porta<span class="qmark close">&rdquo;</span></div>
  <div class="abs author">By Daniel Crowe</div>
  <div class="abs stars"><svg width="92" height="20" viewBox="0 0 92 20" fill="#fff"><g id="s"><polygon points="10,1 12.6,7 19,7.4 14,11.6 15.6,18 10,14.4 4.4,18 6,11.6 1,7.4 7.4,7"/></g><use href="#s" x="24"/><use href="#s" x="48"/><use href="#s" x="72"/></svg></div>
</section>

<footer class="site-footer">
  <div class="abs footer-col" style="left:106px"><h5>QUICK LINKS</h5><ul><li>About Us</li><li>Our Products</li><li>Shop Now</li><li>Testimonials</li></ul></div>
  <div class="abs footer-col" style="left:290px"><h5>RESOURCES</h5><ul><li>Best Price Guarantee</li><li>Coupon Policy</li><li>Help Center</li></ul></div>
  <div class="abs footer-col" style="left:495px;top:60px"><h5>MY ACCOUNT</h5><ul><li>Log In</li><li>Auto-Replenish</li><li>Create Account</li><li>Order History</li><li>Support</li></ul></div>
  <div class="abs footer-col" style="left:671px;top:60px"><h5>RESOURCES</h5><ul><li>FAQ</li><li>Contact Us</li><li>Privay Policy</li><li>Term of Use</li></ul></div>
  <div class="abs footer-col" style="left:865px;top:58px"><h5>EMAIL SIGN UP</h5></div>
  <div class="abs email-field"><svg class="abs" style="left:10px;top:9px" width="14" height="11" viewBox="0 0 14 11"><rect x="0.5" y="0.5" width="13" height="10" fill="#bbb"/><polyline points="0.5,0.5 7,6 13.5,0.5" fill="none" stroke="#fff"/></svg>Enter your email</div>
  <div class="abs subscribe">SUBSCRIBE</div>
  <div class="abs social" style="left:862px"></div>
  <div class="abs social" style="left:898px"></div>
  <div class="abs social" style="left:934px"></div>
  <div class="abs social" style="left:970px"></div>
  <div class="abs paycard" style="left:108px;background:#fff"></div>
  <div class="abs paycard" style="left:162px;background:#6fa6d6"></div>
  <div class="abs paycard" style="left:216px;background:#f2f2f2"></div>
  <div class="abs paycard" style="left:270px;background:#e9a13b"></div>
  <div class="abs paycard" style="left:324px;background:#fff"></div>
</footer>

<div class="copyright">© 2016 Company Name. All right reserved&nbsp; Term of Use</div>

</body>
</html>
```